Bright Stride Clinic helping older adults use exercise as medicine

We need a website for a start up company providing exercise physiology and physiotherapy clinical services for people with serious health conditions such as cancer, diabetes and many others This is an exculsive service with limited time. The 2 main objectives of the website are to create leads for appointments and provide education about the benefits of exercise ie stretches, strength training, cardio vascular improvement for people with health conditions.
Please not too medical in design more fitness and lifestyle... sell the promise, please sell happy fit active people.

Target Market(s)

40-70 year old adults both male and female interested in a healthy lifestyle, ie baby boomers moderate education level (finished high school minimum) rural/country people

Industry/Entity Type

Health

Number of Pages Required

4 page

Font styles to use
Serif
Sans Serif

Colors
f26f22
3176b5

Requirements
Must have
• Website must have a blog/education area and a members area with access to an exercise database (picture, description and video)

```html
<!DOCTYPE html>
<html lang="en">
<head>
<meta charset="utf-8">
<title>Bright Stride Clinic</title>
<link href="https://fonts.googleapis.com/css2?family=Open+Sans:wght@400;600;700&display=swap" rel="stylesheet">
<style>
:root{
  --orange:#f26f22;
  --orange-deep:#e85a10;
  --navy:#0d3a8a;
  --navy-dark:#0a2c6e;
  --blue:#3176b5;
  --grey-bg:#f1f1f1;
  --row-bg:#ececec;
  --text:#555;
  --muted:#888;
  --white:#fff;
}
*{box-sizing:border-box;margin:0;padding:0}
html,body{width:1200px;height:2579px;overflow:hidden}
body{font-family:'Open Sans',sans-serif;color:var(--text);background:var(--white);position:relative}
.abs{position:absolute}

/* hero */
.hero{left:0;top:0;width:1200px;height:923px;overflow:hidden}
.hero-photo{width:100%;height:100%;background:
  radial-gradient(ellipse 420px 360px at 930px 300px,#3a2418 0%,rgba(58,36,24,.85) 45%,rgba(58,36,24,0) 75%),
  radial-gradient(ellipse 520px 300px at 760px 520px,#f0c7a8 0%,rgba(240,199,168,0) 75%),
  linear-gradient(100deg,#6e4a3a 0%,#8a5e48 22%,#d9a887 42%,#f1cdb2 60%,#e3b08f 80%,#c8c0bb 100%)}
.hero-wave{left:0;bottom:0;width:1200px;height:190px}
.hero-caption{right:132px;top:805px;text-align:right;color:var(--white);font-weight:600;font-size:24px;line-height:33px;letter-spacing:.3px}
.dots{left:132px;top:904px;display:flex;gap:4px}
.dots span{width:8px;height:8px;border-radius:50%;background:var(--white)}
.dots span+span{background:#f4b08a}

/* header */
.header{left:131px;top:0;width:938px;height:146px;background:var(--white);overflow:hidden}
.header-swoosh{right:0;top:0;width:420px;height:146px}
.brand{left:16px;top:46px;display:flex;align-items:center;gap:10px}
.brand-dot{width:34px;height:34px;border-radius:50%;background:var(--orange)}
.brand-name{font-size:26px;font-weight:700;color:var(--orange);line-height:1.1;width:190px}
.login{left:273px;top:44px}
.login-title{font-size:14px;font-weight:600;color:#333;display:flex;align-items:center;gap:8px;margin-bottom:15px}
.login-row{display:flex;gap:8px}
.login-row .field{width:139px;height:31px;border:1px solid #ddd;font-size:10px;color:#aaa;padding:9px 8px}
.login-row .field+.field{width:146px}
.login-btn{width:67px;height:31px;background:var(--navy);color:var(--white);font-size:11px;font-weight:700;text-align:center;line-height:31px}
.nav{left:131px;top:146px;width:938px;height:71px;background:linear-gradient(#2a5cb0,#13418f);display:flex}
.nav a{color:var(--white);text-decoration:none;font-size:13px;font-weight:600;display:flex;align-items:center;justify-content:center;border-right:1px solid rgba(255,255,255,.25)}
.nav a:last-child{border-right:none}

/* about */
.eyebrow{left:0;top:962px;width:1200px;text-align:center;font-size:34px;letter-spacing:10px;font-weight:700;color:#c9c9c9}
.section-title{left:0;top:1007px;width:1200px;text-align:center;font-size:26px;font-weight:700;color:var(--navy)}
.intro{left:160px;top:1062px;width:880px;text-align:center;font-size:13px;line-height:24px;color:var(--muted)}
.conditions{left:131px;top:1135px;width:937px;display:grid;grid-template-columns:457px 458px;column-gap:22px;row-gap:9px}
.condition{height:48px;background:var(--row-bg);display:flex;justify-content:space-between;align-items:center;padding:0 16px;font-size:14px;color:#666}
.condition.open{background:var(--orange);color:var(--white);font-weight:600}
.btn{background:var(--navy);color:var(--white);font-weight:700;text-align:center;text-decoration:none;display:block}
.more-btn{left:523px;top:1451px;width:151px;height:53px;line-height:53px;font-size:14px}
.tagline{left:0;top:1526px;width:1200px;text-align:center;font-size:14px;color:var(--orange-deep)}

/* compare */
.compare{left:0;top:1606px;width:1200px;height:624px;background:var(--grey-bg)}
.col{top:52px;width:297px}
.col h3{font-size:19px;font-weight:400;color:#444;line-height:27px;height:103px}
.card{background:var(--white);height:408px;padding:14px;position:relative}
.card-photo{height:205px}
.card ul{list-style:none;margin-top:16px;font-size:12px;line-height:17px;color:#555}
.card li{position:relative;padding-left:18px;margin-bottom:7px}
.card li::before{content:"";position:absolute;left:2px;top:4px;width:9px;height:9px;border-radius:50%;background:var(--orange)}
.card p{margin-top:16px;font-size:12.5px;line-height:21px;color:#555}
.card .btn{position:absolute;left:14px;bottom:30px;width:98px;height:33px;line-height:33px;font-size:11px}

/* blog */
.blog-title{left:0;top:2270px;width:1200px;text-align:center;font-size:27px;font-weight:700;color:var(--navy)}
.post{top:2331px;width:300px;height:110px}
.post-photo{left:0;top:0;width:84px;height:84px}
.post-date{left:0;top:84px;width:84px;height:26px;background:var(--orange);color:var(--white);font-size:12px;font-weight:700;text-align:center;line-height:26px}
.post h4{position:absolute;left:98px;top:2px;font-size:16px;font-weight:700;color:#444;white-space:nowrap}
.post p{position:absolute;left:98px;top:28px;width:190px;font-size:12px;line-height:19px;color:#999}

/* footer */
.footer{left:0;top:2484px;width:1200px;height:95px;background:var(--navy-dark)}
.footer-swoosh{left:0;top:0;width:260px;height:95px}
.copyright{left:224px;top:38px;font-size:12px;color:var(--white)}
.social{left:882px;top:28px;display:flex;gap:13px}
.social span{width:40px;height:40px;border-radius:50%;border:2px solid var(--white);display:flex;align-items:center;justify-content:center}
</style>
</head>
<body>

<section class="hero abs">
  <div class="hero-photo" role="img" aria-label="Woman relaxing during a back massage treatment"></div>
  <svg class="hero-wave abs" viewBox="0 0 1200 190" preserveAspectRatio="none">
    <path d="M0 110 C300 150 650 30 1200 0 L1200 190 L0 190Z" fill="var(--orange)"/>
    <path d="M0 125 C320 165 660 50 1200 22 L1200 190 L0 190Z" fill="var(--navy)"/>
  </svg>
  <div class="hero-caption abs">WE PROVIDE EXERCISE<br>PHYSIOLOGY &amp; PHYSIOTHERAPY<br>CLINICAL SERVICES FOR PEOPLE</div>
  <div class="dots abs"><span></span><span></span><span></span><span></span></div>
</section>

<header class="header abs">
  <svg class="header-swoosh abs" viewBox="0 0 420 146" preserveAspectRatio="none">
    <path d="M20 0 C120 40 200 95 420 120 L420 0Z" fill="var(--navy)"/>
    <path d="M40 0 C140 35 220 82 420 100 L420 0Z" fill="var(--orange)"/>
  </svg>
  <div class="brand abs"><span class="brand-dot"></span><span class="brand-name">Bright Stride Clinic</span></div>
  <div class="login abs">
    <div class="login-title">
      <svg width="14" height="15" viewBox="0 0 14 15"><circle cx="7" cy="4" r="3.5" fill="#555"/><path d="M0 15 C0 9 14 9 14 15Z" fill="#555"/></svg>
      MEMBER LOGIN
    </div>
    <div class="login-row">
      <div class="field">Name:</div>
      <div class="field">Password:</div>
      <div class="login-btn">LOGIN</div>
    </div>
  </div>
</header>

<nav class="nav abs">
  <a href="#" style="width:135px">HOME</a>
  <a href="#" style="width:147px">ABOUT US</a>
  <a href="#" style="width:189px">CLINICAL SERVICES</a>
  <a href="#" style="width:120px">BLOG</a>
  <a href="#" style="width:160px">CONTACT US</a>
  <a href="#" style="width:187px">TESTIMONIALS</a>
</nav>

<div class="eyebrow abs">WHOARETHEY?</div>
<h2 class="section-title abs">WHAT IS AN ACCREDITED EXERCISE PHYSIOLOGIST?</h2>
<p class="intro abs">An Accredited Exercise Physiologist (AEP) holds a four-year equivalent university degree and specialises in the exercise and movement for the prevention and management of chronic diseases and injuries. AEPs provide support for people with:</p>

<div class="conditions abs">
  <div class="condition open"><span>Obesity</span><span>+</span></div>
  <div class="condition"><span>Cancer</span><span>-</span></div>
  <div class="condition"><span>Conditions such as cardiovascular disease</span><span>-</span></div>
  <div class="condition"><span>Chronic pain and fatigue</span><span>-</span></div>
  <div class="condition"><span>Diabetes</span><span>-</span></div>
  <div class="condition"><span>Post-surgical rehabilitation</span><span>-</span></div>
  <div class="condition"><span>Osteoporosis and arthritis</span><span>-</span></div>
  <div class="condition"><span>Neuromuscular exercise therapy</span><span>-</span></div>
  <div class="condition"><span>Mental health conditions</span><span>-</span></div>
  <div class="condition"><span>Pulmonary disease</span><span>-</span></div>
</div>

<a class="btn more-btn abs" href="#">READ MORE</a>
<p class="tagline abs">Most importantly they help people move and exercise their way into a more healthy lifestyle.</p>

<section class="compare abs">
  <div class="col abs" style="left:131px">
    <h3>What makes Accredited Exercise Physiologists different to other exercise professionals?</h3>
    <div class="card">
      <div class="card-photo" role="img" aria-label="Woman in sportswear stretching in a bright gym" style="background:radial-gradient(ellipse 120px 70px at 150px 130px,#3a3a3a,rgba(58,58,58,0) 80%),linear-gradient(180deg,#e9ecef 0%,#cfd6dc 45%,#b9b3ad 100%)"></div>
      <ul>
        <li>They are university qualified</li>
        <li>They undertake strict accreditation requirements</li>
        <li>They are eligible to register with CareLink</li>
      </ul>
      <a class="btn" href="#">READ MORE</a>
    </div>
  </div>
  <div class="col abs" style="left:451px">
    <h3>How are Accredited Exercise Physiologists different from Personal Trainers?</h3>
    <div class="card">
      <div class="card-photo" role="img" aria-label="Client receiving a shoulder massage" style="background:radial-gradient(ellipse 90px 90px at 220px 70px,#5a3a2a,rgba(90,58,42,0) 80%),linear-gradient(135deg,#f7ebe2,#ecc9ae 55%,#f6e4d6)"></div>
      <p>Accredited Exercise Physiologists (AEPs) are university trained and have undertaken extensive training to treat clients with chronic conditions.</p>
      <a class="btn" href="#">READ MORE</a>
    </div>
  </div>
  <div class="col abs" style="left:771px">
    <h3>How are Accredited Exercise Physiologists different from Physiotherapists?</h3>
    <div class="card">
      <div class="card-photo" role="img" aria-label="Woman relaxing on a treatment table" style="background:radial-gradient(ellipse 80px 60px at 90px 110px,#4a2e22,rgba(74,46,34,0) 80%),linear-gradient(180deg,#f4ece6 0%,#e6c3a6 60%,#d9a47f 100%)"></div>
      <p>Accredited Exercise Physiologists and Physiotherapists are both allied health professionals, however AEPs primary focus is to use exercise to prevent.</p>
      <a class="btn" href="#">READ MORE</a>
    </div>
  </div>
</section>

<h2 class="blog-title abs">LATEST BLOG NEWS</h2>

<article class="post abs" style="left:131px">
  <div class="post-photo abs" role="img" aria-label="Massage treatment" style="background:linear-gradient(135deg,#f5e8de,#dcae90)"></div>
  <div class="post-date abs">21 JAN</div>
  <h4>Tortor Purus Mollis loreu</h4>
  <p>Praesent commodo cursilloreoeyus magna, Mcenas fainterduucibus mointerdullis</p>
</article>
<article class="post abs" style="left:455px">
  <div class="post-photo abs" role="img" aria-label="Yoga by the sea" style="background:linear-gradient(180deg,#9fc6de,#dfe9ee 60%,#d6c3a8)"></div>
  <div class="post-date abs">21 JAN</div>
  <h4>Tortor Purus Mollis loreu</h4>
  <p>Praesent commodo cursilloreoeyus magna, Mcenas fainterduucibus mointerdullis</p>
</article>
<article class="post abs" style="left:784px">
  <div class="post-photo abs" role="img" aria-label="Relaxing spa treatment" style="background:linear-gradient(135deg,#f1ddd0,#c58f70)"></div>
  <div class="post-date abs">21 JAN</div>
  <h4>Tortor Purus Mollis loreu</h4>
  <p>Praesent commodo cursilloreoeyus magna, Mcenas fainterduucibus mointerdullis</p>
</article>

<footer class="footer abs">
  <svg class="footer-swoosh abs" viewBox="0 0 260 95" preserveAspectRatio="none">
    <path d="M0 0 L260 0 C180 30 90 60 0 95Z" fill="var(--orange)"/>
    <path d="M0 30 C70 20 150 8 260 0 C170 35 90 70 0 95Z" fill="var(--blue)" opacity=".35"/>
  </svg>
  <div class="copyright abs">Copyright © 2014 all righta are reserved</div>
  <div class="social abs">
    <span aria-label="Social profile"></span>
    <span aria-label="Social profile"></span>
    <span aria-label="RSS feed">
      <svg width="16" height="16" viewBox="0 0 16 16"><circle cx="3" cy="13" r="2" fill="#fff"/><path d="M1 7a8 8 0 0 1 8 8" stroke="#fff" stroke-width="2" fill="none"/><path d="M1 2a13 13 0 0 1 13 13" stroke="#fff" stroke-width="2" fill="none"/></svg>
    </span>
    <span aria-label="Social profile"></span>
    <span aria-label="Social profile"></span>
  </div>
</footer>

</body>
</html>
```